Organizational health infographic

I work as an independent contractor with a larger consulting firm named "the Lantern Works" https://www.lanternworks-example.com/ I need a simple infographic that visually explains the 3 stages of our client engagement, and their respective steps and objectives. Im inclined to use a "subway" map system design (Ive included a a draft overview of the content (in PPT and a PDF) and b) a few sample subway style infographics. I

Target Market(s)

CEOs and Human Resources Officers

Font styles to use
Sans Serif

Colors

Designer to choose colors to be used in the design.

Requirements
Must have
• my contact info
• mark elwin 555-384-9021
• mark.elwin@lanternworksadvisory-example.com
• lantern works logo (I put it near the top center part of the page). Logo and book pictures can be found on the website https://www.lanternworks-example.com
Nice to have
• 1) the more consistent the font and colors are with the Lantern Works website, the better https://www.lanternworks-example.com
• 2) if its possible to have all 3 "subway lines" collapse into a single timeline, that would be cool.
• 3) If its possible to add a visual timeline that shows each stage taking approx 3 to 6 months, also cool.
• 4) in stage 3, Im not sure about whether to use the actual book pictures or simply the titles of each book at a "subway stop" circle.

```html
<!DOCTYPE html>
<html lang="en">
<head>
<meta charset="utf-8">
<title>Lantern Works — Client Engagement Stages</title>
<link href="https://fonts.googleapis.com/css2?family=Montserrat:wght@400;500;600;700&display=swap" rel="stylesheet">
<style>
:root{
  --ink-dark:#2b2e31;
  --ink-deeper:#1f2123;
  --brand-red:#c8102e;
  --brand-pink:#e8457a;
  --navy:#1d2340;
  --white:#ffffff;
  --muted:#c9cbcd;
}
*{margin:0;padding:0;box-sizing:border-box}
html,body{width:1200px;height:1000px;overflow:hidden;background:var(--ink-deeper)}
body{font-family:"Montserrat",Arial,sans-serif;color:var(--white);position:relative}
.top-shade{position:absolute;left:0;top:0;width:1200px;height:50px;background:linear-gradient(#17191a,#2a2d30)}
.header{position:absolute;left:0;top:50px;width:1200px;height:63px;background:var(--white)}
.brand{position:absolute;left:40px;top:10px;display:flex;align-items:center;gap:10px}
.brand-dot{width:38px;height:38px;border-radius:50%;background:var(--brand-red)}
.brand-name{font-size:40px;font-weight:500;color:var(--navy);letter-spacing:-0.5px;line-height:1}
.contact{position:absolute;top:14px;display:flex;align-items:center;gap:9px;color:var(--brand-red);font-weight:500}
.contact-phone{left:493px;font-size:17px}
.contact-email{left:783px;font-size:13.5px}
.contact-icon{width:34px;height:34px;border-radius:50%;background:var(--brand-red);display:flex;align-items:center;justify-content:center}
.red-band{position:absolute;left:0;top:113px;width:1200px;height:32px;background:var(--brand-red)}
.stage-area{position:absolute;left:0;top:145px;width:1200px;height:805px;background:var(--ink-dark)}
.map{position:absolute;left:0;top:0}
.stage-title{position:absolute;left:7px;font-size:16.5px;font-weight:500;line-height:20px}
.legend-title{position:absolute;left:10px;top:757px;font-size:16px;font-weight:500}
.legend-item{position:absolute;left:41px;font-size:9.5px;font-weight:600;line-height:11px}
.panel{position:absolute;left:957px;width:225px}
.panel-narrow{width:180px}
.panel h3{font-size:13px;font-weight:600;margin-bottom:12px}
.panel h4{font-size:9.5px;font-weight:600;color:var(--white);line-height:11.2px}
.panel p{font-size:9.5px;color:var(--muted);line-height:11.2px}
.panel .gap{height:13px}
.panel .small-gap{height:11px}
.panel .mid-gap{height:15px}
</style>
</head>
<body>
<div class="top-shade"></div>
<header class="header">
  <div class="brand"><span class="brand-dot"></span><span class="brand-name">lantern works</span></div>
  <div class="contact contact-phone">
    <span class="contact-icon"><svg width="14" height="20" viewBox="0 0 14 20"><rect x="1.5" y="1.5" width="11" height="17" rx="2" fill="none" stroke="#fff" stroke-width="2"/><line x1="5" y1="15.5" x2="9" y2="15.5" stroke="#fff" stroke-width="1.5"/></svg></span>
    <span>Mark Elwin 555-384-9021</span>
  </div>
  <div class="contact contact-email">
    <span class="contact-icon"><svg width="18" height="13" viewBox="0 0 18 13"><rect x="0" y="0" width="18" height="13" rx="1.5" fill="#fff"/><polyline points="1,1 9,7.5 17,1" fill="none" stroke="#c8102e" stroke-width="1.6"/></svg></span>
    <span>mark.elwin@lanternworksadvisory-example.com</span>
  </div>
</header>
<div class="red-band"></div>
<div class="stage-area"></div>

<svg class="map" width="1200" height="1000" viewBox="0 0 1200 1000" font-family="Montserrat, Arial, sans-serif">
  <defs>
    <linearGradient id="edge-fade" x1="0" y1="0" x2="1" y2="0"><stop offset="0" stop-color="#fff"/><stop offset="1" stop-color="#c8102e"/></linearGradient>
    <linearGradient id="slant-fade" x1="0" y1="0" x2="0" y2="1"><stop offset="0" stop-color="#c8102e"/><stop offset="1" stop-color="#e8457a"/></linearGradient>
    <linearGradient id="bar-fade" x1="0" y1="0" x2="1" y2="0"><stop offset="0" stop-color="#d42a62"/><stop offset="1" stop-color="#ffffff"/></linearGradient>
    <g id="timeline">
      <rect x="0" y="0" width="690" height="15" rx="7.5" fill="#fff"/>
      <rect x="0" y="0" width="8" height="15" fill="#fff"/>
      <rect x="104" y="0" width="14" height="15" fill="#2b2e31"/>
      <rect x="222" y="0" width="13" height="15" fill="#2b2e31"/>
      <rect x="340" y="0" width="12" height="15" fill="#c8102e"/>
      <rect x="458" y="0" width="12" height="15" fill="#c8102e"/>
      <rect x="575" y="0" width="12" height="15" fill="#c8102e"/>
      <g font-size="9.5" font-weight="700" fill="#2b2e31" text-anchor="middle">
        <text x="52" y="11">1 Month</text><text x="170" y="11">2 Month</text><text x="288" y="11">3 Month</text>
        <text x="405" y="11">4 Month</text><text x="522" y="11">5 Month</text><text x="638" y="11">6 Month</text>
      </g>
    </g>
    <g id="side-panel">
      <polygon points="830,0 845,0 920,240 905,240" fill="url(#slant-fade)"/>
      <rect x="905" y="240" width="295" height="13" fill="url(#bar-fade)"/>
    </g>
  </defs>

  <use href="#side-panel" y="160"/>
  <use href="#side-panel" y="428"/>
  <use href="#side-panel" y="697"/>

  <g fill="none" stroke="url(#edge-fade)" stroke-width="4">
    <polyline points="0,198 207,198 220,152"/>
    <polyline points="0,466 207,466 220,421"/>
    <polyline points="0,741 207,741 212,700"/>
  </g>
  <line x1="210" y1="742" x2="146" y2="935" stroke="url(#slant-fade)" stroke-width="4"/>

  <use href="#timeline" y="398"/>
  <use href="#timeline" y="674"/>
  <use href="#timeline" y="934"/>

  <g stroke="#fff" stroke-width="4" fill="none">
    <line x1="82" y1="269" x2="478" y2="269"/>
    <polyline points="490,290 490,343 412,343 412,522" stroke-dasharray="11 7"/>
    <polyline points="686,558 686,640 306,640 306,824" stroke-dasharray="11 7"/>
    <polyline points="412,538 456,494 648,494 682,535"/>
    <polyline points="412,538 458,577 646,577 682,545"/>
    <polyline points="306,840 340,803 690,803 712,832"/>
    <polyline points="306,840 340,876 690,876 712,850"/>
  </g>

  <g stroke="#fff" stroke-width="4">
    <circle cx="82" cy="269" r="14" fill="#2b2e31"/>
    <circle cx="184" cy="269" r="16" fill="#fff"/>
    <circle cx="286" cy="269" r="16" fill="#fff"/>
    <circle cx="388" cy="269" r="14" fill="#2b2e31"/>
    <polygon points="474,257 506,257 490,285" fill="#2b2e31" stroke-linejoin="round"/>
  </g>
  <g stroke="#fff" stroke-width="4">
    <circle cx="412" cy="538" r="14" fill="#2b2e31"/>
    <circle cx="456" cy="494" r="14" fill="#2b2e31"/>
    <circle cx="551" cy="494" r="14" fill="#2b2e31"/>
    <circle cx="648" cy="494" r="14" fill="#2b2e31"/>
    <circle cx="458" cy="577" r="14" fill="#2b2e31"/>
    <circle cx="520" cy="577" r="16" fill="#fff"/>
    <circle cx="583" cy="577" r="16" fill="#fff"/>
    <circle cx="646" cy="577" r="14" fill="#2b2e31"/>
    <polygon points="670,528 702,528 686,556" fill="#2b2e31" stroke-linejoin="round"/>
  </g>
  <g stroke="#fff" stroke-width="4">
    <circle cx="306" cy="840" r="14" fill="#2b2e31"/>
    <rect x="342" y="789" width="30" height="30" fill="#2b2e31"/>
    <rect x="342" y="861" width="30" height="30" fill="#2b2e31"/>
    <polygon points="701,827 733,827 717,856" fill="#2b2e31" stroke-linejoin="round"/>
  </g>

  <rect x="412" y="751" width="32" height="53" fill="#c41e2a" role="img" aria-label="Workshop book cover"/>
  <rect x="484" y="753" width="30" height="51" fill="#d8dadc" role="img" aria-label="Workshop book cover"/>
  <rect x="555" y="753" width="32" height="51" fill="#e6ebee" role="img" aria-label="Workshop book cover"/>
  <rect x="624" y="752" width="32" height="52" fill="#b39a3f" role="img" aria-label="Workshop book cover"/>
  <rect x="513" y="824" width="43" height="52" fill="#c82a2e" role="img" aria-label="Training guide book cover"/>

  <g font-size="9.5" fill="#e6e6e6">
    <text x="47" y="245">meeting audits</text>
    <text x="249" y="299">leader coaching</text>
    <text x="349" y="245">Quarterly offsites</text>
    <text x="387" y="542" text-anchor="end">Key leader kick off</text>
    <text x="508" y="524">Key leader conferences</text>
    <text x="440" y="554">meeting audits</text>
    <text x="345" y="582">Department teams</text>
    <text x="482" y="608">Leader coaching</text>
    <text x="597" y="610">Department rollouts</text>
    <text x="331" y="777">workshops</text>
    <text x="208" y="842">Playbook rollout</text>
    <text x="330" y="853">Internal training</text>
    <text x="414" y="867">Train the trainers</text>
    <text x="414" y="893">Train the leaders</text>
  </g>

  <g stroke="#fff" stroke-width="3">
    <circle cx="21" cy="803" r="7.5" fill="#2b2e31"/>
    <circle cx="21" cy="839" r="9" fill="#fff"/>
    <polygon points="13,867 29,867 21,882" fill="#2b2e31" stroke-linejoin="round"/>
    <rect x="13" y="903" width="16" height="15" fill="#2b2e31"/>
  </g>
</svg>

<div class="stage-title" style="top:150px">Stage 1<br>Executive launch</div>
<div class="stage-title" style="top:419px">Stage 2<br>Next level rollout</div>
<div class="stage-title" style="top:695px">Stage 3<br>Organizational rollout</div>

<div class="legend-title">Legend</div>
<div class="legend-item" style="top:798px">Live offsite</div>
<div class="legend-item" style="top:834px">Video conference</div>
<div class="legend-item" style="top:864px">Transition<br>evaluation</div>
<div class="legend-item" style="top:905px">Training</div>

<section class="panel" style="top:183px">
  <h3>Objectives</h3>
  <p>Team cohesion</p><p>Solid trust</p><p>Aligned expectations</p><p>Playbook 1.0</p>
  <p>Aligned vision, values, strategy, priorities &amp; roles</p>
  <p>Productive meetings</p><p>Consistent communication with greater org</p>
  <div class="gap"></div>
  <h3>Transition readness</h3>
  <p>Cohesion validation (CTAR)</p><p>Playbook complete</p><p>Meeting momentum</p>
</section>

<section class="panel" style="top:427px">
  <h3>Objectives</h3>
  <h4>Key leaders</h4>
  <p>Finish Playbook 2.0</p><p>Become Ambassadors of Org Health</p><p>Cross functional cooperation</p>
  <div class="small-gap"></div>
  <h4>Department teams</h4>
  <p>Cohesion, Clarity, productive meetings</p>
  <div class="small-gap"></div>
  <h4>Department rollouts</h4>
  <p>Break down silos</p><p>Dept priorities align to org priorities</p>
  <div class="mid-gap"></div>
  <h3>Transition readiness</h3>
  <p>Department CTARs</p><p>core values detailed and implemented</p><p>meeting mastery</p>
</section>

<section class="panel panel-narrow" style="top:736px">
  <h3>Objectives</h3>
  <h4>All employees</h4>
  <p>Understand and utilize the Playbook</p>
  <p>Are equipped &amp; motivated to create a healthy culture</p>
  <div class="mid-gap"></div>
  <h3>Transition redadlness</h3>
  <p>The consultation is completed when the leaders are ready to assume responsibility forintaining a healthy culture</p>
</section>
</body>
</html>
```